Zorvath GmbH banner ad

Banner ad for Facebook Our company name (logo) Title: Transporter and bus rental Text: Without deposit, super prices

Target Market(s)

Rental

Requirements
Must have
• LOGO from us, Evt. A pair of transporters in the picture

```html
<!DOCTYPE html>
<html lang="de">
<head>
<meta charset="utf-8">
<title>Zorvath GmbH – Transporter &amp; Bus Vermietung</title>
<link href="https://fonts.googleapis.com/css2?family=Arimo:wght@400;700&family=Tinos:wght@400&display=swap" rel="stylesheet">
<style>
  :root{
    --navy:#0d0d7a;
    --royal:#1a1ac0;
    --mist:#d5dae3;
    --mist-light:#e9ecf1;
    --paper:#ffffff;
    --ink:#111111;
    --stage:#ececec;
    --photo-light:#f6dc93;
    --photo-main:#eeb63a;
  }
  *{box-sizing:border-box;margin:0;padding:0}
  html,body{width:1200px;height:619px;overflow:hidden;background:var(--stage)}
  .banner{
    position:absolute;left:40px;top:76px;width:1120px;height:467px;
    background:var(--paper);overflow:hidden;
    font-family:"Arimo",Arial,sans-serif;
  }
  .banner-shapes{position:absolute;inset:0;width:100%;height:100%}
  .headline-top{
    position:absolute;left:37px;top:58px;width:362px;height:73px;
    background:var(--mist);color:var(--navy);
    font-size:41px;line-height:73px;padding-left:14px;white-space:nowrap;
  }
  .headline-bus{
    position:absolute;left:37px;top:131px;width:258px;height:89px;
    background:var(--navy);color:var(--paper);
    font-weight:700;font-size:76px;line-height:89px;padding-left:14px;
    box-shadow:inset 0 0 0 4px var(--navy),inset 0 0 0 7px var(--paper);
  }
  .headline-rent{
    position:absolute;left:37px;top:219px;width:376px;height:72px;
    background:var(--navy);color:var(--paper);
    font-weight:700;font-size:44px;line-height:72px;padding-left:14px;
    font-variant:small-caps;letter-spacing:2px;white-space:nowrap;
    box-shadow:inset 0 0 0 4px var(--navy),inset 0 0 0 7px var(--paper);
  }
  .perks{
    position:absolute;left:0;top:327px;width:454px;height:53px;
    border:2px solid var(--ink);background:var(--paper);
    font-family:"Tinos","Times New Roman",serif;font-size:30px;color:var(--ink);
    display:flex;align-items:center;gap:14px;padding-left:38px;white-space:nowrap;
  }
  .perk::before{
    content:"";display:inline-block;width:9px;height:9px;border-radius:50%;
    background:var(--navy);margin-right:6px;vertical-align:middle;
  }
  .brand{
    position:absolute;left:862px;top:40px;display:flex;align-items:center;gap:10px;
    color:var(--navy);font-weight:700;font-size:28px;letter-spacing:1px;white-space:nowrap;
  }
  .brand-square{width:28px;height:28px;background:var(--navy)}
  .vehicle-photo{
    position:absolute;left:626px;top:102px;width:480px;height:352px;
    background:radial-gradient(ellipse at 45% 50%,var(--photo-main) 0%,var(--photo-light) 55%,var(--paper) 100%);
  }
</style>
</head>
<body>
<div class="banner">
  <svg class="banner-shapes" viewBox="0 0 720 300" preserveAspectRatio="none" aria-hidden="true">
    <polygon points="404,0 450,0 330,232 314,232" fill="var(--mist)"/>
    <polygon points="376,0 404,0 312,234 296,234" fill="var(--navy)"/>
    <polygon points="296,234 330,232 440,300 300,300" fill="var(--mist-light)"/>
    <polygon points="0,274 408,274 432,300 0,300" fill="var(--navy)"/>
    <polygon points="0,282 380,282 398,300 0,300" fill="var(--royal)" opacity="0.45"/>
    <polygon points="160,84 200,84 240,60 230,84" fill="var(--mist)"/>
    <polygon points="60,186 100,186 84,200" fill="var(--mist)"/>
  </svg>

  <div class="headline-top">Transporter &amp;</div>
  <div class="headline-bus">BUS</div>
  <div class="headline-rent">Vermietung</div>

  <div class="perks">
    <span class="perk">Ohne Kaution</span>
    <span class="perk">Superpreise</span>
  </div>

  <div class="brand">
    <span class="brand-square"></span>
    <span>ZORVATH</span>
  </div>

  <div class="vehicle-photo" role="img" aria-label="Foto eines gelben Linienbusses in Schrägansicht von vorne"></div>
</div>
</body>
</html>
```